Tab-Fix Notes
3inx3in Tab Fix Notes with "Thank You!" message
Tab-Fix Notes - Corporate Services
Creative Brief
In need of designs for 3inch x 3inch Tab Fix Notes. Company Branding and Image (professional, high energy, uplifting, splash of color) The words "Thank You" and company website (www.marlowbrekke.com) must be included on actual tab fix.
Corporate Services
Corporate and professional, but modern.
3inch by 3 inch tab fix size. Use your creativity to the fullest but handwritten notes must legible on tab-fix. White backgrounds are okay as long as message stands out. Color preference of background - hot pink, orange, neon blue, neon green The words "Thank You" and company website (www.marlowbrekke.com) must be included on actual tab fix.
Related Contests
Social Media Banner Design (for Chatterloop, Zanvio+, Peepwire, and WorkNexa) based on current website.
Concepts
The Beacon Planning Institute Banner Display

```html
<!DOCTYPE html>
<html lang="en">
<head>
<meta charset="utf-8">
<title>Tab-Fix Notes – Thank You</title>
<link href="https://fonts.googleapis.com/css2?family=Open+Sans:wght@400;600;700&display=swap" rel="stylesheet">
<style>
  :root {
    --stage: #e9e9eb;
    --paper: #ffffff;
    --paper-shade: #ececec;
    --ink-grey: #7a7a7a;
    --brand-red: #d9261c;
    --brand-orange: #f08a1c;
    --swoosh: #cfcfcf;
    --note-size: 440px;
  }
  * { box-sizing: border-box; margin: 0; padding: 0; }
  html, body { width: 1200px; height: 926px; overflow: hidden; }
  body {
    background: var(--stage);
    font-family: "Open Sans", Arial, sans-serif;
    display: flex;
    align-items: center;
    justify-content: center;
    gap: 80px;
  }
  .note {
    position: relative;
    width: var(--note-size);
    height: var(--note-size);
    background: linear-gradient(160deg, var(--paper) 55%, var(--paper-shade));
    overflow: hidden;
  }
  .note-footer { position: absolute; inset: 0; width: 100%; height: 100%; }
  .handwritten-message {
    position: absolute;
    left: 34px; top: 34px;
    width: 360px; height: 260px;
    border-radius: 6px;
    background: linear-gradient(180deg, #f1f1f3, #e6e6ea);
  }
  .brand-name {
    position: absolute;
    right: 26px; top: 318px;
    display: flex; align-items: center; gap: 6px;
    font-size: 15px; font-weight: 700;
    line-height: 20px;
    color: var(--brand-orange);
  }
  .brand-name .dot {
    width: 10px; height: 10px; border-radius: 50%;
    background: var(--brand-red);
  }
</style>
</head>
<body>

  <section class="note note--written">
    <div class="handwritten-message" role="img" aria-label="Handwritten thank-you message to a client, signed by hand"></div>
    <svg class="note-footer" viewBox="0 0 440 440">
      <path d="M0 398 C150 393 310 383 440 360" fill="none" stroke="var(--swoosh)" stroke-width="2"/>
      <path d="M0 406 C150 401 320 391 440 372 L440 440 L0 440Z" fill="var(--brand-orange)"/>
      <path d="M0 415 C150 411 320 401 440 385 L440 440 L0 440Z" fill="var(--brand-red)"/>
      <text x="22" y="382" font-size="28" fill="var(--ink-grey)" font-family="Open Sans, Arial, sans-serif">Thank You</text>
      <text x="420" y="432" font-size="13" font-weight="700" fill="#ffffff" text-anchor="end" font-family="Open Sans, Arial, sans-serif">www.marlowbrekke.com</text>
    </svg>
    <div class="brand-name"><span class="dot"></span>Marlow Brekke</div>
  </section>

  <section class="note note--blank">
    <svg class="note-footer" viewBox="0 0 440 440">
      <path d="M0 398 C150 393 310 383 440 360" fill="none" stroke="var(--swoosh)" stroke-width="2"/>
      <path d="M0 406 C150 401 320 391 440 372 L440 440 L0 440Z" fill="var(--brand-orange)"/>
      <path d="M0 415 C150 411 320 401 440 385 L440 440 L0 440Z" fill="var(--brand-red)"/>
      <text x="22" y="382" font-size="28" font-family="Open Sans, Arial, sans-serif"><tspan fill="var(--brand-red)">Thank </tspan><tspan fill="var(--brand-orange)">You!</tspan></text>
      <text x="420" y="432" font-size="13" font-weight="700" fill="#ffffff" text-anchor="end" font-family="Open Sans, Arial, sans-serif">www.marlowbrekke.com</text>
    </svg>
    <div class="brand-name"><span class="dot"></span>Marlow Brekke</div>
  </section>

</body>
</html>
```